Wine Label for a Sweet Wine Called "Glimmo"

We need a wine label that will be used for both a sweet red and a sweet white wine. The very important thing to remember is the target market for these wines is: young American women who love sweet wines and they also spend a lot of their money on their hair, clothes, jewelry, nails. They LOVE Glimmo (Glimmo is a word used to describe flashy accessories, jewelry, decoration.) This label needs to be eye catching, showy, fun, glittery. Please put the brand name, "Glimmo," big, and then in smaller but still readable words underneath the label or somewhere on the label: Sweet, Sophisticated, Red (or white). (An example of what I mean is attached). To differentiate between the two color wines you can suggest color changes to differentiate between the red label and the white label but the label design itself should be the same. Ultimately, the label can be the exact same label for both white and red as long as it looks good on a white wine (a greenish/yellow wine in a clear glass bottle) and a red wine (a dark color wine in a dark bottle).

I've attached an example of the text size relationship between the word Glimmo and the words to go underneath or elsewhere on the label, but you can certainly play with this-- it is just a suggestion of the text size relationship, and definitely NOT at all mandatory that you use any of these fonts.

You can pick the size of the label but try to stay within normal wine label sizes, meaning don't go bigger than approx. 3.5 inches wide and 5 inches tall.

Target Market(s)

Young American women who love sweet wines and spend a lot of money on their hair, clothes, jewelry, nails. They love Glimmo (Glimmo is a word that means flashy accessories, jewelry, decoration)

Requirements
Must have
• It needs to be flashy, glittery, fun, eye catching, memorable
Nice to have
• It shouldn't be too too ultra feminine! The target market is strong independent women and we also have men who will buy it too.

```html
<!DOCTYPE html>
<html lang="en">
<head>
<meta charset="utf-8">
<title>Glimmo Sweet White – Label Options</title>
<link rel="stylesheet" href="https://fonts.googleapis.com/css2?family=Cinzel:wght@400;700;900&family=Playfair+Display:wght@400&display=swap">
<style>
  :root {
    --page-bg: #ffffff;
    --label-black: #080808;
    --gold: #d8bd84;
    --gold-light: #f3e2b4;
    --gold-deep: #8c6f3f;
    --silver: #b8b8b8;
    --silver-deep: #6e6e6e;
    --text-light: #c9ae76;
  }
  * { box-sizing: border-box; margin: 0; padding: 0; }
  html, body {
    width: 1200px;
    height: 1200px;
    overflow: hidden;
    background: var(--page-bg);
  }
  .label-set {
    position: absolute;
    inset: 0;
    display: flex;
    justify-content: center;
    align-items: center;
    gap: 40px;
  }
  .label {
    position: relative;
    width: 340px;
    height: 390px;
    background: var(--label-black);
    overflow: hidden;
    box-shadow: 0 0 0 1px #000;
  }
  .label-frame {
    position: absolute;
    inset: 0;
    width: 340px;
    height: 390px;
  }

  .corner-ornament {
    position: absolute;
    width: 40px; height: 40px;
  }
  .corner-ornament.tl { left: 12px; top: 12px; background: linear-gradient(135deg, var(--gold-light), var(--gold-deep) 45%, rgba(140,111,63,0) 75%); }
  .corner-ornament.tr { right: 12px; top: 12px; background: linear-gradient(225deg, var(--gold-light), var(--gold-deep) 45%, rgba(140,111,63,0) 75%); }
  .corner-ornament.bl { left: 12px; bottom: 12px; background: linear-gradient(45deg, var(--gold-light), var(--gold-deep) 45%, rgba(140,111,63,0) 75%); }
  .corner-ornament.br { right: 12px; bottom: 12px; background: linear-gradient(315deg, var(--gold-light), var(--gold-deep) 45%, rgba(140,111,63,0) 75%); }

  .scroll-cluster {
    position: absolute;
    left: 50%;
    transform: translateX(-50%);
    border-radius: 50%;
  }
  .scroll-cluster.top {
    top: 8px; width: 250px; height: 118px;
    background: radial-gradient(ellipse at center, var(--gold-light) 0%, var(--gold) 35%, var(--gold-deep) 62%, rgba(140,111,63,0) 72%);
  }
  .scroll-cluster.bottom {
    bottom: 8px; width: 250px; height: 118px;
    background: radial-gradient(ellipse at center, var(--gold-light) 0%, var(--gold) 35%, var(--gold-deep) 62%, rgba(140,111,63,0) 72%);
  }
  .scroll-side {
    position: absolute;
    top: 95px;
    width: 70px; height: 200px;
    border-radius: 50%;
    background: radial-gradient(ellipse at center, var(--silver) 0%, var(--silver-deep) 45%, rgba(110,110,110,0) 72%);
  }
  .scroll-side.left { left: 4px; }
  .scroll-side.right { right: 4px; }

  .brand {
    position: absolute;
    left: 0; right: 0;
    text-align: center;
    font-family: "Cinzel", serif;
    font-weight: 900;
    color: var(--gold);
    line-height: 1;
  }
  .variety {
    position: absolute;
    left: 0; right: 0;
    text-align: center;
    font-family: "Cinzel", serif;
    font-weight: 700;
    color: var(--gold);
    line-height: 1;
  }
  .tagline {
    position: absolute;
    left: 0; right: 0;
    text-align: center;
    font-family: "Cinzel", serif;
    font-size: 9px;
    letter-spacing: 1px;
    color: var(--text-light);
    line-height: 1;
  }

  .label--classic .variety { top: 127px; font-size: 8px; letter-spacing: 1.5px; }
  .label--classic .brand { top: 170px; font-size: 44px; letter-spacing: 1px; }
  .label--classic .tagline { top: 334px; }

  .label--deco .brand { top: 166px; font-size: 40px; letter-spacing: 1px; }
  .label--deco .variety { top: 222px; font-size: 13px; letter-spacing: 2px; }
  .label--deco .tagline { top: 344px; }

  .label--baroque .brand { top: 170px; font-size: 38px; font-weight: 700; color: var(--silver); letter-spacing: 3px; }
  .label--baroque .tagline {
    top: 216px;
    font-family: "Playfair Display", serif;
    font-size: 10px;
    letter-spacing: 0.6px;
  }
</style>
</head>
<body>
<main class="label-set">

  <section class="label label--classic">
    <svg class="label-frame" viewBox="0 0 340 390" aria-hidden="true">
      <defs>
        <linearGradient id="gold-sheen-a" x1="0" y1="0" x2="1" y2="1">
          <stop offset="0" stop-color="#f3e2b4"/>
          <stop offset="0.5" stop-color="#c9a96a"/>
          <stop offset="1" stop-color="#8c6f3f"/>
        </linearGradient>
      </defs>
      <rect x="10" y="10" width="320" height="370" fill="none" stroke="url(#gold-sheen-a)" stroke-width="0.8"/>
      <rect x="38" y="118" width="264" height="124" rx="62" fill="none" stroke="url(#gold-sheen-a)" stroke-width="2"/>
      <rect x="46" y="125" width="248" height="110" rx="55" fill="none" stroke="url(#gold-sheen-a)" stroke-width="0.8"/>
      <line x1="130" y1="140" x2="210" y2="140" stroke="url(#gold-sheen-a)" stroke-width="0.8"/>
      <rect x="110" y="222" width="120" height="4" fill="url(#gold-sheen-a)"/>
      <line x1="100" y1="320" x2="240" y2="320" stroke="url(#gold-sheen-a)" stroke-width="0.6"/>
    </svg>
    <div class="corner-ornament tl" role="img" aria-label="Gold filigree corner flourish"></div>
    <div class="corner-ornament tr" role="img" aria-label="Gold filigree corner flourish"></div>
    <div class="corner-ornament bl" role="img" aria-label="Gold filigree corner flourish"></div>
    <div class="corner-ornament br" role="img" aria-label="Gold filigree corner flourish"></div>
    <p class="variety">White</p>
    <h1 class="brand">GLIMMO</h1>
    <p class="tagline">SWEET | SOPHISTICATED</p>
  </section>

  <section class="label label--deco">
    <svg class="label-frame" viewBox="0 0 340 390" aria-hidden="true">
      <defs>
        <linearGradient id="gold-sheen-b" x1="0" y1="0" x2="0" y2="1">
          <stop offset="0" stop-color="#f3e2b4"/>
          <stop offset="0.5" stop-color="#c9a96a"/>
          <stop offset="1" stop-color="#8c6f3f"/>
        </linearGradient>
      </defs>
      <rect x="10" y="10" width="320" height="370" fill="none" stroke="url(#gold-sheen-b)" stroke-width="0.8"/>
      <path d="M110 60 H230 V100 H292 V290 H230 V330 H110 V290 H48 V100 H110 Z" fill="none" stroke="url(#gold-sheen-b)" stroke-width="2"/>
      <path d="M118 68 H222 V108 H284 V282 H222 V322 H118 V282 H56 V108 H118 Z" fill="none" stroke="url(#gold-sheen-b)" stroke-width="0.8"/>
      <path d="M140 108 Q170 68 200 108" fill="none" stroke="url(#gold-sheen-b)" stroke-width="1.2"/>
      <path d="M140 282 Q170 322 200 282" fill="none" stroke="url(#gold-sheen-b)" stroke-width="1.2"/>
      <line x1="170" y1="78" x2="170" y2="108" stroke="url(#gold-sheen-b)" stroke-width="1"/>
      <line x1="170" y1="282" x2="170" y2="312" stroke="url(#gold-sheen-b)" stroke-width="1"/>
      <line x1="70" y1="150" x2="270" y2="150" stroke="url(#gold-sheen-b)" stroke-width="0.6"/>
      <rect x="120" y="216" width="100" height="24" fill="#2a2418" stroke="url(#gold-sheen-b)" stroke-width="1"/>
    </svg>
    <div class="corner-ornament tl" role="img" aria-label="Gold filigree corner flourish"></div>
    <div class="corner-ornament tr" role="img" aria-label="Gold filigree corner flourish"></div>
    <div class="corner-ornament bl" role="img" aria-label="Gold filigree corner flourish"></div>
    <div class="corner-ornament br" role="img" aria-label="Gold filigree corner flourish"></div>
    <h1 class="brand">GLIMMO</h1>
    <p class="variety">WHITE</p>
    <p class="tagline">SWEET | SOPHISTICATED</p>
  </section>

  <section class="label label--baroque">
    <div class="scroll-cluster top" role="img" aria-label="Baroque gold scrollwork crest"></div>
    <div class="scroll-side left" role="img" aria-label="Silver baroque scroll flourish"></div>
    <div class="scroll-side right" role="img" aria-label="Silver baroque scroll flourish"></div>
    <div class="scroll-cluster bottom" role="img" aria-label="Baroque gold scrollwork crest"></div>
    <h1 class="brand">GLIMMO</h1>
    <p class="tagline">Sweet | Sophisticated | White</p>
  </section>

</main>
</body>
</html>
```